Business Card Design for Kestrelwood Carpentry

I need a business card design for my carpentry company Kestrelwood Carpentry. Ive attached files with all information I require on both sides. Look forward to seeing your design.

```html
<!DOCTYPE html>
<html lang="en">
<head>
<meta charset="utf-8">
<title>Kestrelwood Carpentry – Business Card</title>
<link href="https://fonts.googleapis.com/css2?family=Barlow+Semi+Condensed:wght@500;600&family=Oswald:wght@600&display=swap" rel="stylesheet">
<style>
  :root {
    --backdrop: #b4b4b4;
    --card-light: #e8e8e6;
    --card-dark: #2b2a29;
    --ink: #2a2a2a;
    --accent: #e2582c;
    --light-text: #eeeeec;
  }
  * { margin: 0; padding: 0; box-sizing: border-box; }
  html, body {
    width: 1200px; height: 1071px; overflow: hidden;
    background: var(--backdrop);
    font-family: "Barlow Semi Condensed", Arial, sans-serif;
  }
  .card {
    position: absolute; left: 210px; width: 774px; height: 428px;
    box-shadow: 0 2px 6px rgba(0,0,0,.25);
  }
  .card-front { top: 86px; background: var(--card-light); }
  .card-back { top: 562px; background: var(--card-dark); overflow: hidden; }

  .brand-mark {
    position: absolute; top: 56px; left: 339px;
    width: 96px; height: 96px; border-radius: 50%;
    background: var(--accent);
  }
  .brand {
    position: absolute; left: 0; right: 0; text-align: center;
    font-family: "Oswald", Arial, sans-serif; font-weight: 600;
    text-transform: uppercase; line-height: 1;
  }
  .card-front .brand { top: 172px; font-size: 40px; letter-spacing: 4px; color: var(--ink); }
  .card-back .brand { top: 62px; font-size: 38px; letter-spacing: 3px; color: var(--light-text); }

  .phone {
    position: absolute; top: 294px; left: 0; right: 0; text-align: center;
    font-family: "Oswald", Arial, sans-serif; font-weight: 600;
    font-size: 56px; line-height: 1; letter-spacing: 2px; color: var(--ink);
  }
  .tagline {
    position: absolute; top: 358px; left: 0; right: 0; text-align: center;
    font-weight: 600; font-size: 25px; line-height: 1.2; color: var(--accent);
  }

  .services {
    position: absolute; top: 184px; left: 0; right: 0;
    list-style: none; text-align: center;
  }
  .services li {
    font-weight: 600; font-size: 25px; line-height: 40px; color: var(--light-text);
  }
  .services span::before {
    content: ""; display: inline-block; width: 5px; height: 5px;
    background: var(--accent); margin: 0 6px 5px 2px; vertical-align: middle;
  }

  .card-footer {
    position: absolute; left: 0; right: 0; bottom: 0; height: 53px;
    background: var(--card-light); color: var(--ink);
    display: flex; align-items: center; justify-content: center; gap: 20px;
    font-weight: 500; font-size: 25px;
  }
  .sep { width: 4px; height: 4px; background: var(--ink); }
</style>
</head>
<body>
  <section class="card card-front">
    <span class="brand-mark"></span>
    <div class="brand">Kestrelwood Carpentry</div>
    <p class="phone">0400 555 271</p>
    <p class="tagline">Anything Carpentry, Anywhere In Sydney, Bla Bla 01234</p>
  </section>

  <section class="card card-back">
    <div class="brand">Kestrelwood Carpentry</div>
    <ul class="services">
      <li><span>Decks and Pergolas</span> <span>Shop Fitouts</span> <span>Wall and Roef Framing</span></li>
      <li><span>Refurbishments</span> <span>Doors and Wirclaws</span> <span>Fences / Gates</span></li>
      <li><span>Attic Conversions</span> <span>Privacy Screens</span> <span>Timber Flooring</span></li>
      <li><span>Wall Cladding</span> <span>Extensions &amp; MORE</span></li>
    </ul>
    <div class="card-footer">
      <span>Lic # 190482K</span><span class="sep"></span><span>www.kestrelwoodcarpentry@mail.com</span>
    </div>
  </section>
</body>
</html>
```